Wordpress Design Project (Halvern)

We need a wordpress design for an established auction and real estate company based in Virginia. The winning design will incorporate the colors of logo (red and black) creatively with an accent color in a very professional and clean layout.

Industry/Entity Type

Real Estate

Requirements
Must have
• We will require winning designer to provide a layered PSD (Adobe photoshop) concept file, along with any non-standard font files used.

Horizontal Navigation menu with these links:
Home - Upcoming Auctions - Past Auctions - For Sale- Consignments - About Us - Highlights - Contact Us

A slideshow element on the home page using the placeholder image provided.

Sidebar widgets to be included are: Email sign-up form - Featured Auctions - Featured Assets for Sale (see attached for visual of these widgets)

attached logos in footer with company contact info

```html
<!DOCTYPE html>
<html lang="en">
<head>
<meta charset="utf-8">
<title>Halvern Enterprises</title>
<link href="https://fonts.googleapis.com/css2?family=Arimo:wght@400;700&family=Questrial&display=swap" rel="stylesheet">
<style>
:root{
  --red:#f2473a;
  --red-dark:#c9362c;
  --ink:#2a1414;
  --text:#4a4a4a;
  --pink:#f6e6e6;
  --pink-line:#f0d6d6;
  --page:#fbf1f1;
  --grey-btn:#6d6d6d;
}
*{box-sizing:border-box;margin:0;padding:0}
html,body{width:1150px;height:1200px;overflow:hidden}
body{
  position:relative;
  font-family:"Arimo",Arial,sans-serif;
  color:var(--text);
  background:linear-gradient(180deg,#f7e2e2 0,#fdf7f7 300px,#fdf6f6 100%);
}
.column{position:absolute;left:85px;top:0;width:980px;height:1120px;background:linear-gradient(180deg,rgba(255,255,255,0) 0,rgba(255,255,255,.55) 100px,rgba(255,255,255,.55) 100%)}
.abs{position:absolute;white-space:nowrap}
.display{font-family:"Questrial","Century Gothic",sans-serif;font-weight:400}
.accent{color:var(--red)}

/* header */
.brand{left:85px;top:24px;display:flex;align-items:center;gap:12px}
.brand-mark{width:56px;height:56px;background:var(--red)}
.brand-name{font-family:"Questrial",sans-serif;font-size:44px;color:var(--ink);letter-spacing:1px}
.call{left:665px;top:40px;font-size:20px;font-weight:700;color:var(--ink)}
.call span{color:var(--red)}
.search{left:885px;top:35px;width:180px;height:33px;border:1px solid #ddd;background:#fff;font-size:11px;color:#777;padding:10px}
.search svg{position:absolute;right:10px;top:8px}

/* nav */
.nav{left:90px;top:104px;width:969px;height:51px;display:flex;border-radius:6px 6px 0 0;overflow:hidden;
  background:linear-gradient(180deg,#f76a5e 0,var(--red) 100%);box-shadow:0 0 0 3px #fff}
.nav a{color:#fff;text-decoration:none;font-size:14px;font-weight:700;display:flex;align-items:center;justify-content:center;border-right:1px solid #d8463b;text-shadow:0 1px 1px rgba(0,0,0,.2)}
.nav a.current{background:linear-gradient(180deg,#d85549,var(--red-dark))}
.nav a:last-child{border-right:0}

/* slider */
.slider{left:90px;top:165px;width:969px;height:347px;background:var(--pink)}
.slide-img{left:97px;top:172px;width:955px;height:334px;
  background:linear-gradient(180deg,#8fb0dc 0,#bcd0e6 38%,#5a7a4a 40%,#5a6f82 46%,#6f84a0 70%,#7d8f5b 82%,#4f6a33 100%)}
.caption{left:111px;top:443px;width:517px;height:45px;background:rgba(30,30,30,.82);color:#fff;font-size:18.5px;line-height:45px;padding:0 17px;font-family:"Questrial",sans-serif;overflow:hidden}
.caption-next{left:632px;top:443px;width:38px;height:45px;background:rgba(30,30,30,.82)}

/* service tiles */
.tile{top:533px;width:312px;height:197px;background:var(--pink)}
.tile .photo{position:absolute;left:5px;top:5px;width:302px;height:146px}
.tile h3{position:absolute;left:12px;top:164px;font-size:18px;color:var(--ink);white-space:nowrap}

/* welcome */
.welcome h2{font-size:20.5px;color:var(--ink)}
.upcoming h2{font-size:19.5px;color:var(--ink)}
.welcome{left:97px;top:756px;width:627px;white-space:normal}
.welcome p{font-size:13px;line-height:22px;text-align:justify;margin-top:8px;color:#555}
.welcome h2{margin-bottom:10px}

.upcoming{left:750px;top:757px;width:307px}
.up-box{left:749px;top:797px;width:308px;height:191px;background:var(--pink)}
.up-thumb{left:760px;top:807px;width:115px;height:78px;border:2px solid #555;background:linear-gradient(180deg,#8ab0c8,#c9ced3 50%,#7b8a6b)}
.session{left:885px;top:805px;font-size:13px;line-height:22px;color:#444}
.more{left:885px;top:853px;width:155px;height:31px;background:linear-gradient(180deg,#8a8a8a,var(--grey-btn));color:#fff;font-weight:700;font-size:14px;text-align:center;line-height:31px;border:1px solid #555;border-radius:2px}
.meta{left:760px;font-size:13px;line-height:22px;color:#444}

/* partners & newsletter */
.rule{left:96px;width:959px;height:1px;background:#ddd}
.partners-label{left:102px;top:1052px;font-size:16px;color:var(--ink)}
.badge{background:#555}
.divider{left:595px;top:1030px;width:1px;height:65px;background:#ddd}
.news-label{left:615px;top:1052px;font-size:16px;color:var(--ink)}
.news-input{left:735px;top:1042px;width:318px;height:41px;background:var(--pink-line);font-size:12px;color:#666;padding:14px 20px}
.news-go{left:1021px;top:1049px;width:27px;height:27px;border-radius:50%;background:#fff;border:1px solid #bbb}

/* footer */
.foot-links{left:93px;top:1131px;font-size:12.5px;color:#555}
.copyright{left:93px;top:1161px;font-size:12px;color:#555;word-spacing:2px}
.social{top:1142px;width:23px;height:23px;border-radius:3px}
</style>
</head>
<body>
<div class="column"></div>

<header>
  <div class="abs brand"><span class="brand-mark"></span><span class="brand-name">Halvern</span></div>
  <div class="abs call">Call us : <span>555 208 7714</span></div>
  <div class="abs search">Search
    <svg width="16" height="16" viewBox="0 0 16 16"><circle cx="6" cy="6" r="4.5" fill="none" stroke="#222" stroke-width="2.2"/><line x1="9.5" y1="9.5" x2="14" y2="14" stroke="#222" stroke-width="3"/></svg>
  </div>
</header>

<nav class="abs nav">
  <a class="current" style="width:84px" href="#">Home</a>
  <a style="width:177px" href="#">Upcoming Auctions</a>
  <a style="width:136px" href="#">Past Auctions</a>
  <a style="width:98px" href="#">For Sale</a>
  <a style="width:139px" href="#">Consignments</a>
  <a style="width:106px" href="#">About Us</a>
  <a style="width:111px" href="#">Highlights</a>
  <a style="width:118px" href="#">Contact Us</a>
</nav>

<section>
  <div class="abs slider"></div>
  <div class="abs slide-img" role="img" aria-label="Lake shoreline with a wooden dock and trees under a blue sky"></div>
  <div class="abs caption">We are an established auction and real estate company</div>
  <div class="abs caption-next"><svg width="38" height="45" viewBox="0 0 38 45"><path d="M12 12 L24 22.5 L12 33" fill="none" stroke="#fff" stroke-width="5"/></svg></div>
</section>

<section>
  <div class="abs tile" style="left:90px">
    <div class="photo" role="img" aria-label="Row of townhouses" style="background:linear-gradient(180deg,#7fa8d8 0,#e6dcc0 45%,#c9b98f 80%,#6b7d4b 100%)"></div>
    <h3 class="display"><span class="accent">REAL ESTATE</span> SERVICES</h3>
  </div>
  <div class="abs tile" style="left:418px">
    <div class="photo" role="img" aria-label="Silver hatchback car" style="background:radial-gradient(ellipse at 50% 55%,#9a9ea3 0,#c9cbcd 30%,#fff 60%)"></div>
    <h3 class="display"><span class="accent">OTHER</span> SERVICES</h3>
  </div>
  <div class="abs tile" style="left:745px">
    <div class="photo" role="img" aria-label="Customer support agents wearing headsets" style="background:linear-gradient(90deg,#d7dde3 0,#c8c3c0 50%,#e8d2c4 100%)"></div>
    <h3 class="display"><span class="accent">CONTACT</span> US</h3>
  </div>
</section>

<section class="abs welcome">
  <h2 class="display"><span class="accent">Welcome to</span> Halvern</h2>
  <p>Donec molestie sapien sit amet libero sollicitudin in aliquam tortor egestas. Suspendisse varius, ligula non tempor condimentum, lorem turpis placerat quam, id auctor dolor sem et velit. Duis feugiat imperdiet semper. Ut vehicula leo et ligula molestie accumsan eget non lacus.</p>
  <p>Proin sodales lorem quis leo vestibulum a egestas lectus pulvinar. Suspendisse pellentesque sem vitae massa aliquet pellentesque. Aenean tincidunt mollis erat, ut placerat leo luctus quis. Morbi purus sem, malesuada et consectetur vel, scelerisque id massa. Sed sit amet felis ipsum. Maecenas mattis adipiscing suscipit. Cum sociis natoque penatibus et magnis dis parturient montes, nascetur ridiculus mus. Phasellus ligula eros, aliquet vel ullamcorper ac, mattis ultricies augue. Praesent quis ultricies urna. Vestibulum porttitor, tellus at ultrices euismod, metus lacus ullamcorper felis, et venenatis nulla mi sed ante.</p>
</section>

<aside>
  <div class="abs upcoming"><h2 class="display"><span class="accent">Upcoming</span> Auctions</h2></div>
  <svg class="abs" style="left:1035px;top:759px" width="14" height="18" viewBox="0 0 14 18"><path d="M3 2 L10 9 L3 16" fill="none" stroke="#999" stroke-width="3"/></svg>
  <div class="abs up-box"></div>
  <div class="abs up-thumb" role="img" aria-label="Silver minivan"></div>
  <div class="abs session">Session 1 :<br><span class="accent">Multi Estate &amp; Consignment</span></div>
  <div class="abs more">MORE DETAILS</div>
  <div class="abs meta" style="top:895px">Start Date/ Time :<br><span class="accent">Wednesday, April 10, 2013 at 2:00 PM</span></div>
  <div class="abs meta" style="top:939px">Location :<br><span class="accent">1180 Willow Bend Lane, Carrow, VA 23077</span></div>
</aside>

<section>
  <div class="abs rule" style="top:1024px"></div>
  <div class="abs partners-label display"><span class="accent">Our</span> Patrners</div>
  <div class="abs badge" style="left:221px;top:1047px;width:25px;height:28px"></div>
  <div class="abs badge" style="left:276px;top:1054px;width:58px;height:18px;border-radius:3px;background:#777"></div>
  <div class="abs badge" style="left:362px;top:1053px;width:58px;height:16px;border-radius:8px;background:#888"></div>
  <div class="abs badge" style="left:445px;top:1046px;width:37px;height:37px;border-radius:50%;background:#5a6fa8"></div>
  <div class="abs badge" style="left:500px;top:1050px;width:68px;height:26px;background:#d8432f"></div>
  <div class="abs divider"></div>
  <div class="abs news-label display"><span class="accent">Our</span> Newsletter</div>
  <div class="abs news-input">Enter your mail ID</div>
  <div class="abs news-go"><svg width="27" height="27" viewBox="0 0 27 27"><path d="M11 8 L16 13.5 L11 19" fill="none" stroke="#333" stroke-width="2.6"/></svg></div>
  <div class="abs rule" style="top:1102px"></div>
</section>

<footer>
  <div class="abs foot-links">Home - Upcoming Auctions - Past Auctions - For Sale- Consignments - About Us - Highlights - Contact Us</div>
  <div class="abs copyright">Copyright &nbsp;© &nbsp;2013 &nbsp;&nbsp;www.halvern.com &nbsp;&nbsp;All rights reserved.</div>
  <div class="abs social" style="left:1004px;background:#3b5998"></div>
  <div class="abs social" style="left:1034px;background:#4fb8e8"></div>
</footer>
</body>
</html>
```